Webdesign für Personalvermittlung
Zielgruppe
Personalvermittlung
Aufgabenstellung
es soll einladend - nicht zu überladen und natürlich cool und modern sein

```html
<!DOCTYPE html>
<html lang="de">
<head>
<meta charset="utf-8">
<title>pflegeweg job – Personalvermittlung</title>
<link href="https://fonts.googleapis.com/css2?family=Roboto:wght@400;500;700&family=Kaushan+Script&family=Source+Serif+4:wght@400;600&display=swap" rel="stylesheet">
<style>
:root{
  --green:#6cc04a;
  --green-dark:#3f9a2a;
  --orange:#f7931e;
  --blue:#29a8e0;
  --pink:#d63384;
  --pink-dark:#7a1e4a;
  --cyan:#c4f0f5;
  --cyan-band:#a9e3ea;
  --ink:#1d1d1d;
  --muted:#6d6d6d;
  --line:#dcdcdc;
  --star:#f6c12b;
}
*{box-sizing:border-box;margin:0;padding:0}
html,body{width:1200px;height:3214px;overflow:hidden;background:#fff}
body{position:relative;font-family:'Roboto',sans-serif;color:var(--ink)}
.abs{position:absolute}
.bar{left:0;width:1200px;height:10px;background:var(--green)}
.brand{display:flex;align-items:center;gap:10px;font-size:28px;font-weight:500;color:#333}
.brand-dot{width:44px;height:44px;border-radius:50%;background:var(--green)}
.nav{top:96px;left:640px;display:flex;gap:56px;font-size:20px;font-weight:500}
.nav .active{color:var(--orange)}
.photo{border-radius:2px}
.hero-photo{left:47px;top:198px;width:602px;height:403px;background:linear-gradient(135deg,#6f6a64,#b9b2a6 55%,#3c3a37)}
.hero-text{left:708px;top:192px;width:450px;font-size:13.5px;line-height:22px}
.hero-text h1{font-size:22px;color:var(--blue);font-weight:700;margin-bottom:10px}
.hero-text h2{font-size:17px;color:var(--orange);font-weight:700;margin-bottom:14px}
.checks{list-style:none;margin:12px 0 18px}
.checks li{display:flex;align-items:center;gap:6px}
.checks svg{width:15px;height:15px}
.btn{display:flex;align-items:center;justify-content:center;background:var(--green);color:#fff;font-size:13px;font-weight:500;border-radius:6px;height:34px}
.band{left:47px;top:677px;width:1105px;height:264px;background:linear-gradient(180deg,var(--cyan),var(--cyan-band))}
.band-photo{left:80px;top:688px;width:200px;height:253px;background:linear-gradient(180deg,#e9e3dc,#f7f7f7);border-radius:100px 100px 0 0}
.band-text{left:362px;top:718px;width:750px;text-align:center;font-size:14px;line-height:17px}
.band-text p{margin-bottom:16px}
.expect-left{left:0;top:941px;width:542px;height:622px;background:#f6f8f9}
.expect-right{left:542px;top:941px;width:658px;height:622px;background:var(--cyan)}
.expect-title{left:0;width:1396px;top:1016px;text-align:center;font-size:21px;font-weight:700;color:var(--orange)}
.expect-title span{color:var(--green-dark)}
.feature{width:205px;text-align:center;font-size:12px;line-height:15px}
.feature h3{font-size:15px;color:var(--green);font-weight:700;margin-bottom:16px;line-height:18px}
.contact-photo{left:47px;top:1617px;width:603px;height:429px;background:linear-gradient(135deg,#c9c6c0,#8a7868 50%,#d8d4cf)}
.contact-title{left:712px;top:1694px;font-size:17px;font-weight:700;color:var(--blue)}
.field{border:1px solid var(--line);padding:0 20px;display:flex;align-items:center;font-size:15px;color:var(--muted)}
.testi-title{left:130px;top:2157px;font-size:17px;font-weight:700;color:var(--pink)}
.avatar{width:62px;height:62px;border-radius:50%;background:linear-gradient(180deg,#6a4a3a,#d9b59a);border:2px solid #ccc}
.bubble{height:40px;border-radius:10px;background:linear-gradient(90deg,var(--pink),var(--pink-dark));color:#fff;font-family:'Source Serif 4',serif;font-size:13px;display:flex;align-items:center;padding:0 12px;white-space:nowrap;overflow:hidden}
.stars{color:var(--star);font-size:20px;letter-spacing:1px}
.who{font-family:'Source Serif 4',serif;font-weight:600;font-size:12.5px}
.dot{width:14px;height:14px;border-radius:50%;background:#f1d8e4}
.info{font-size:12.5px;font-weight:700;line-height:15px}
.info a{color:var(--green-dark)}
.info .val{color:var(--green-dark)}
.info svg{width:20px;height:20px;position:absolute;left:-34px;top:-3px}
.map{left:606px;top:2579px;width:546px;height:183px;background:linear-gradient(135deg,#eef1f3,#e3ecd9 60%,#f1efe9)}
.footer{left:0;top:2849px;width:1200px;height:353px;background:linear-gradient(180deg,#eef3f6,#c8d2d9 60%,#aab7c1)}
.slogan{left:0;top:3062px;width:1200px;text-align:center;font-family:'Kaushan Script',cursive;font-size:40px;color:var(--orange)}
.copy{left:0;top:3180px;width:1200px;text-align:center;font-size:10px}
</style>
</head>
<body>
<div class="abs bar" style="top:0"></div>

<div class="abs brand" style="left:47px;top:92px"><span class="brand-dot"></span>pflegeweg job</div>
<nav class="abs nav"><span class="active">Home</span><span>Wir bieten dir</span><span>Über uns</span><span>Kontakt</span></nav>

<div class="abs photo hero-photo" role="img" aria-label="Foto: Zwei Geschäftsleute schütteln sich im Büro die Hand"></div>
<div class="abs hero-text">
  <h1>Dein Nächster Karriereschritt Im Pflegeberuf!</h1>
  <h2>Willkommen Bei PFLEGEWEG-JOB.De</h2>
  <p>Wir Bieten Ihnen Den Perfekten<br>Job Als Führungskraft!<br>Du Bist:</p>
  <ul class="checks">
    <li style="margin-left:0"><svg viewBox="0 0 16 16"><rect x="1" y="2" width="12" height="12" fill="none" stroke="#6cc04a" stroke-width="2"/><path d="M4 8l3 3 7-8" fill="none" stroke="#6cc04a" stroke-width="2"/></svg>Wohnbereichsleiter/In</li>
    <li style="margin-left:16px"><svg viewBox="0 0 16 16"><rect x="1" y="2" width="12" height="12" fill="none" stroke="#6cc04a" stroke-width="2"/><path d="M4 8l3 3 7-8" fill="none" stroke="#6cc04a" stroke-width="2"/></svg>Pflegedienstleiter/In</li>
    <li style="margin-left:33px"><svg viewBox="0 0 16 16"><rect x="1" y="2" width="12" height="12" fill="none" stroke="#6cc04a" stroke-width="2"/><path d="M4 8l3 3 7-8" fill="none" stroke="#6cc04a" stroke-width="2"/></svg>Stationsleiter/In</li>
    <li style="margin-left:50px"><svg viewBox="0 0 16 16"><rect x="1" y="2" width="12" height="12" fill="none" stroke="#6cc04a" stroke-width="2"/><path d="M4 8l3 3 7-8" fill="none" stroke="#6cc04a" stroke-width="2"/></svg>OP-Manager/In</li>
    <li style="margin-left:68px"><svg viewBox="0 0 16 16"><rect x="1" y="2" width="12" height="12" fill="none" stroke="#6cc04a" stroke-width="2"/><path d="M4 8l3 3 7-8" fill="none" stroke="#6cc04a" stroke-width="2"/></svg>Heimleiter/In</li>
    <li style="margin-left:86px"><svg viewBox="0 0 16 16"><rect x="1" y="2" width="12" height="12" fill="none" stroke="#6cc04a" stroke-width="2"/><path d="M4 8l3 3 7-8" fill="none" stroke="#6cc04a" stroke-width="2"/></svg>Klinikdirektor/In</li>
  </ul>
  <p>Und Willst Dich Verändern?<br>Oder Möchtest Eine Weiterbildung In Die Management-Ebene?</p>
</div>
<div class="abs btn" style="left:708px;top:567px;width:192px">Ich Will Ein Angebot</div>
<div class="abs btn" style="left:960px;top:567px;width:192px">Kontaktiere Uns</div>

<div class="abs band"></div>
<div class="abs band-photo" role="img" aria-label="Foto: Ärztin im weißen Kittel reicht die Hand"></div>
<div class="abs band-text">
  <p>Mit Mehr Als 15 Jahren Erfahrung In Der Vermittlung Von Fach- Und Führungskräften, Steht Ihnen Das Team Von Pflegeweg-Job.De Als Vertrauensvoller Partner Bei Ihrem Jobwechsel Zur Seite.</p>
  <p>Gemeinsam Finden Wir Die Ideale Stelle, Welche Auf Grund Ihrer Persönlichen Wünsche Und Vorstellungen Am Besten Zu Ihnen Passt.</p>
  <p>Lehnen Sie Sich Bequem Zurück Und Überlassen Das Finden Ihres Neuen Arbeitsplatzes Uns.</p>
  <p>Am Ende Des Tage Entscheiden Sie, Ob Ein Vorstellungsgespräch Stattfinden Soll Oder Wir Für Sie Weitersuchen!</p>
</div>

<div class="abs expect-left"></div>
<div class="abs expect-right"></div>
<div class="abs btn" style="left:960px;top:925px;width:192px">Ich Will Ein Angebot</div>
<div class="abs expect-title">Was Darfst Du Von <span>PFLEGEWEG-JOB.De</span> Erwarten?</div>

<div class="abs feature" style="left:443px;top:1108px"><h3>Zugriff Auf Mehr Stellen</h3>In Zusammenarbeit Mit Einrichtungen Und Kliniken Erhalten Unsere Kandidaten Einen Zugesicherten Bonus In Höhe Von 750 EUR Für Das Vertrauen Bei Ihrem Jobwechsel In Pflegeweg-Job.De</div>
<div class="abs feature" style="left:706px;top:1108px"><h3>Anonymität</h3>Wir Erstellen Ein Profil Deiner Kenntnisse Und Fähigkeiten Sowie Deiner Berufserfahrung. Weder Dein Name, Noch Deine Vorarbeitgeber Tauchen Im Ersten Schritt Auf. Erst Wenn Eine Einrichtung Oder Klinik Daran Interesse Zeigt, Entscheiden Wir Gemeinsam, Wie Es Weitergeht!</div>
<div class="abs feature" style="left:958px;top:1108px"><h3>Dauerhafte Betreuung</h3>Dein Neuer Arbeitgeber Hält Nicht Was Er Verspricht? Keine Sorge, Wir Werden Für Dich Sofort Wieder Aktiv Und Bieten Dir Schnell Neue Möglichkeiten An - Ohne Dass Du Erneut Bewerbungen Versenden Musst! Ein Anruf Oder Eine Email Genügt!</div>
<div class="abs feature" style="left:443px;top:1323px"><h3>Alle Versprechungen Findest Du Im Arbeitsvertrag</h3>Du Stellst Bedingungen An Deinen Neuen Arbeitgeber? - Dann Sorgen Wir Gemeinsam Dafür, Dass Du Diese Auch Im Arbeitsvertrag Findest - Zu Deiner Sicherheit. Nichts Ist Schlimmer, Als Leere Versprechungen!</div>
<div class="abs feature" style="left:706px;top:1359px"><h3>100% Kostenfrei</h3>Unsere Dienstleistung Ist Für Dich Als Bewerber 100% Kostenfrei! Es Gibt Auch Garantiert Keine Versteckten Kosten!</div>
<div class="abs feature" style="left:958px;top:1359px"><h3>Keine Zeitarbeit</h3>Wir Vermitteln Ausschließlich In Festanstellungen Direkt Bei Kliniken Oder Einrichtungen. Wir Können Dir Jedoch Wertvolle Tipps Geben, Sollte Zeitarbeit Für Dich In Frage Kommen ...WIR KENNEN UNS AUS!</div>
<div class="abs btn" style="left:716px;top:1546px;width:191px">Ich Will Ein Angebot</div>

<div class="abs photo contact-photo" role="img" aria-label="Foto: Junges Team, ein Mann zeigt nach vorne"></div>
<div class="abs contact-title">Nimm Ganz Einfach Kontakt Zu Uns Auf:</div>
<div class="abs field" style="left:692px;top:1761px;width:186px;height:42px">Name</div>
<div class="abs field" style="left:965px;top:1761px;width:186px;height:42px">Nachname</div>
<div class="abs field" style="left:692px;top:1821px;width:186px;height:43px">Mobile</div>
<div class="abs field" style="left:965px;top:1821px;width:186px;height:43px">Email</div>
<div class="abs field" style="left:692px;top:1887px;width:459px;height:45px">Notiz</div>
<div class="abs btn" style="left:693px;top:1983px;width:135px;height:35px;font-size:16px;color:#1d1d1d;border-radius:3px">Anmelden</div>
<div class="abs" style="left:853px;top:1992px;font-size:13px;color:var(--muted)">Oder Kontaktieren Sie Uns Unter</div>
<div class="abs" style="left:1078px;top:1978px;width:40px;height:40px;border-radius:50%;background:var(--green)"></div>

<div class="abs testi-title">Erfahrungen unserer Bewerber: Was sie mit uns erlebt haben</div>

<div class="abs avatar" style="left:47px;top:2235px" role="img" aria-label="Illustration: Avatar einer Bewerberin"></div>
<div class="abs bubble" style="left:125px;top:2236px;width:606px">“Lorem ipsum dolor sit amet consectetur. Ut id et eleifend adipiscing.”</div>
<div class="abs stars" style="left:125px;top:2276px">★★★★★</div>
<div class="abs who" style="left:670px;top:2282px">Lena K.</div>

<div class="abs avatar" style="left:858px;top:2235px" role="img" aria-label="Illustration: Avatar einer Bewerberin"></div>
<div class="abs bubble" style="left:935px;top:2236px;width:217px;border-radius:10px 0 0 10px">“Lorem ipsum dolor sit amet consectetur.</div>
<div class="abs stars" style="left:935px;top:2276px">★★★★★</div>

<div class="abs avatar" style="left:47px;top:2334px" role="img" aria-label="Illustration: Avatar einer Bewerberin"></div>
<div class="abs bubble" style="left:125px;top:2335px;width:606px">Lorem ipsum dolor sit amet consectetur. Viverra dui tortor posuere bibendum. Auctor feugiat”.</div>
<div class="abs stars" style="left:125px;top:2375px">★★★★★</div>
<div class="abs who" style="left:670px;top:2381px">Lena K.</div>

<div class="abs avatar" style="left:858px;top:2334px" role="img" aria-label="Illustration: Avatar einer Bewerberin"></div>
<div class="abs bubble" style="left:935px;top:2335px;width:217px;border-radius:10px 0 0 10px">“Lorem ipsum dolor sit amet consectetur.</div>
<div class="abs stars" style="left:935px;top:2375px">★★★★★</div>

<div class="abs dot" style="left:633px;top:2471px;background:var(--pink)"></div>
<div class="abs dot" style="left:673px;top:2471px"></div>
<div class="abs dot" style="left:714px;top:2471px"></div>

<div class="abs info" style="left:82px;top:2622px">
  <svg viewBox="0 0 20 20"><path d="M4 2l4 1 1 4-2 2a11 11 0 004 4l2-2 4 1 1 4-2 2C9 18 2 11 2 4z" fill="#111"/></svg>
  Telefon: <span class="val">01234 567 890 1</span></div>
<div class="abs info" style="left:82px;top:2653px">
  <svg viewBox="0 0 20 20"><rect x="2" y="4" width="16" height="11" fill="#111"/><path d="M2 4l8 6 8-6" fill="none" stroke="#fff" stroke-width="1.5"/></svg>
  Email: &nbsp;<a href="#">info@pflegeweg-job.de</a></div>
<div class="abs info" style="left:82px;top:2684px">
  <svg viewBox="0 0 20 20"><path d="M10 1a6 6 0 00-6 6c0 5 6 12 6 12s6-7 6-12a6 6 0 00-6-6z" fill="#111"/><circle cx="10" cy="7" r="2.3" fill="#fff"/></svg>
  Adresse: <a href="#">Lindenhof 12, 10115</a><br><a href="#" style="margin-left:51px">Musterstadt</a></div>

<div class="abs info" style="left:345px;top:2622px">Inhaber &nbsp;<span class="val">Herr Jonas Brenner</span></div>
<div class="abs info" style="left:345px;top:2653px">Telefon: <span class="val">01234 567 890 1</span></div>
<div class="abs info" style="left:345px;top:2684px">Email: &nbsp;<a href="#">jonas.brenner@pflegeweg-job.de</a></div>

<div class="abs map" role="img" aria-label="Karte: Standort des Büros"></div>

<div class="abs footer" role="img" aria-label="Foto: Händedruck vor Stadtsilhouette, aufgehellt"></div>
<div class="abs" style="left:555px;top:2910px;width:84px;height:84px;border-radius:50%;background:var(--green)"></div>
<div class="abs" style="left:0;top:3006px;width:1192px;text-align:center;font-size:32px;font-weight:500;color:#333">pflegeweg job</div>
<div class="abs slogan">Wir bauen gemeinsam an Ihrer Zukunft</div>
<div class="abs copy">© 2024 Alle Rechte Vorbehalten</div>
<div class="abs bar" style="top:3204px"></div>
</body>
</html>
```